Re-design my 1-page website to be BETTER!

Hi Guys,
I recently created a 1-page website for market testing purposes for a company I am starting. Problem is, the feedback i've had on the page is its a bit corporate and boring.
I would love you to design something that is fresher, more modern and will generate leads (via the sign up CTA's).
Here is the website as it is now: www.guidelinkhub.com.au.
If you need any info or have questions, just reach out.
Thanks,
Oliver

Target Market(s)

Entrepreneurs

Number of Pages Required

1 page

Font styles to use
Sans Serif

Colors
abd036
34a6d7
ffffff

Requirements
Must have
• Fresh, Modern, high-converting
• I expect 70% of traffic to be mobile so must be mobile optimised first.
Nice to have
• I've highlighted colours i like below, however, I am open to suggestions. I like colours that are gender neutral and show energy and vibrancy.
• I have used Proxima Nova for the fonts, as I find it easy to read however, I am open to suggestions. My main preference is that it displays well and is easily read

```html
<!DOCTYPE html>
<html lang="en">
<head>
<meta charset="utf-8">
<title>GuideLink Hub</title>
<link rel="stylesheet" href="https://fonts.googleapis.com/css2?family=Figtree:wght@300;400;500;600;700&display=swap">
<style>
  :root {
    --lime: #abd036;
    --sky: #34a6d7;
    --white: #ffffff;
    --heading-blue: #4a7f9c;
    --body-ink: #3f3f44;
    --hero-green: #8cbb7a;
    --hero-teal: #4f9aa6;
    --halo: #dce9f5;
    --accent-cyan: #9fdde3;
    --board: #4a4755;
  }
  * { box-sizing: border-box; margin: 0; padding: 0; }
  html, body { width: 1200px; height: 1200px; overflow: hidden; background: var(--white); }
  body { font-family: "Figtree", sans-serif; position: relative; }

  .hero {
    position: absolute; left: 0; top: 0; width: 1200px; height: 642px;
    background: linear-gradient(110deg, #a8cc88 0%, var(--hero-green) 35%, #6fa89a 65%, var(--hero-teal) 100%);
  }
  .brand {
    position: absolute; left: -18px; top: 46px;
    font-size: 24px; font-weight: 300; letter-spacing: 1.5px;
    color: var(--lime); text-transform: uppercase;
  }
  .nav { position: absolute; top: 50px; left: 0; width: 1200px; }
  .nav a {
    position: absolute; color: var(--white); text-decoration: none;
    font-size: 14px; font-weight: 400;
  }
  .nav a.is-active::after {
    content: ""; position: absolute; left: -6px; right: -4px; top: 29px;
    height: 2px; background: var(--white);
  }
  .nav-cta {
    position: absolute; left: 1112px; top: 41px; width: 140px; height: 39px;
    border: 2px solid var(--lime); border-radius: 20px;
    color: var(--white); font-size: 9px; font-weight: 700; letter-spacing: 1px;
    padding: 13px 0 0 24px; text-transform: uppercase;
  }
  .hero-copy { position: absolute; left: 0; top: 220px; width: 1200px; text-align: center; color: var(--white); }
  .eyebrow {
    display: inline-flex; align-items: center; gap: 12px;
    font-size: 13px; font-weight: 700; letter-spacing: 1.4px; text-transform: uppercase;
  }
  .eyebrow::before, .eyebrow::after { content: ""; width: 18px; height: 1px; background: rgba(255,255,255,.6); }
  .hero-title { font-size: 64px; font-weight: 600; line-height: 1; margin-top: 19px; letter-spacing: .5px; }
  .hero-quote { width: 350px; margin: 24px auto 0; font-size: 15px; line-height: 22.4px; }
  .hero-cta {
    display: inline-block; margin-top: 53px; width: 206px; height: 56px; border-radius: 28px;
    background: var(--lime); color: var(--white); font-size: 22px; font-weight: 600; line-height: 56px;
  }

  .halo {
    position: absolute; left: 798px; top: 420px; width: 900px; height: 900px; border-radius: 50%;
    background: linear-gradient(180deg, #d9eaf7, var(--halo));
  }
  .spark { position: absolute; left: 1082px; top: 1163px; width: 78px; height: 78px; border-radius: 50%; background: var(--accent-cyan); }
  .intro { position: absolute; left: 133px; top: 806px; width: 340px; }
  .intro-title { font-size: 48px; font-weight: 600; line-height: 58px; color: var(--heading-blue); }
  .intro-text { margin-top: 26px; font-size: 20px; line-height: 32px; color: var(--body-ink); }
  .teaching-art {
    position: absolute; left: 582px; top: 820px; width: 556px; height: 380px;
    background: var(--board); border-top: 12px solid #c8a064; border-left: 12px solid #c8a064; border-right: 12px solid #c8a064;
  }
</style>
</head>
<body>
  <header class="hero">
    <div class="hero-photo" role="img" aria-label="Young entrepreneur on a laptop talking with a mentor, tinted green and teal"></div>
    <div class="brand">GuideLink Hub</div>
    <nav class="nav">
      <a style="left:720px">Home</a>
      <a class="is-active" style="left:810px">Features</a>
      <a style="left:914px">Blog</a>
      <a style="left:990px">Articles</a>
    </nav>
    <div class="nav-cta">Get Started</div>
    <div class="hero-copy">
      <div class="eyebrow">A Mentor for Everyone</div>
      <h1 class="hero-title">GuideLink Hub</h1>
      <p class="hero-quote">"We've flipped the model on its head -&nbsp; so now you choose your Mentor.&nbsp; It's never been this easy to get the advice and guidance you need to thrive</p>
      <a class="hero-cta">Get Started</a>
    </div>
  </header>

  <div class="halo"></div>
  <section class="intro">
    <h2 class="intro-title">Finding a Mentor Has Never Been Easier</h2>
    <p class="intro-text">Having a great Mentor will turbo-charge your personal, professional or business growth.&nbsp; But unless you have an incredible network, finding one is tough.</p>
  </section>
  <div class="teaching-art" role="img" aria-label="Illustration of a teacher pointing at a chalkboard reading mentor for everyone"></div>
  <div class="spark"></div>
</body>
</html>
```